Bench Advertisement - We Buy Houses Design Needed

Need a catchy, simple but elegant design for bus benches to advertise our company.

We need our website, or phone number, and a smal description (1-2 bulletpoints of what we do and what we offer)

The tricky part is for the designer to fit everything and make the website name as part of the title and fitting everything so that people passing by on the street can see what we offer.

Our website is quickhomebuyerdesk.com - (916) 482-3091

Something simple but something that catches the eye of walking pedestrians, and drivers driving by the bench.

Our company buys houses, any condition, any situation, we buy houses for cash and close quickly. You can use this description to create a few bulletpoints however you like. Must follow dimensions in attachment.

Target Market(s)

People in foreclosure, about to lose their homes, people that need a quick cash sale of their property

Industry/Entity Type

Real Estate

Requirements
Must have
• catchy, website name, phone number, few brief bulletpoints about what we offer, colors that will catch peoples eye while walking or driving - advertisement will be placed on bus benches - visit our website to see the type of houses we buy - Also have more work for winner of design with possible bonuses
Nice to have
• Feel free to use description or images on our website - make sure the description is just bullet points and it fits with the overall theme / size of the advertisement - Bold bright colors - put yourself in their shoes (if you were going through financial difficulties and about to lose your house to foreclosure or auction, what would you want to see to pick up the phone and call us for a quick sale of your house?) (or if you have a house that you are having a problem with, problem renters, unkept/beat up house, what would make you want to call us and sell your house to us?)

```html
<!DOCTYPE html>
<html lang="en">
<head>
<meta charset="utf-8">
<title>Quick Home Buyer Desk – Bench Advertisement</title>
<link href="https://fonts.googleapis.com/css2?family=Source+Sans+3:wght@400;600;700&family=PT+Sans+Narrow&display=swap" rel="stylesheet">
<style>
  :root {
    --teal: #3f8c9b;
    --teal-light: #5ea9b5;
    --teal-dark: #3a8797;
    --ink-grey: #6a6a6a;
    --paper: #ffffff;
    --backdrop: #2a2a2a;
  }
  * { margin: 0; padding: 0; box-sizing: border-box; }
  html, body {
    width: 1200px; height: 768px; overflow: hidden;
    background: var(--backdrop);
  }
  .bench-ad {
    position: absolute; left: 0; top: 217px;
    width: 1200px; height: 334px;
    background: var(--paper);
    overflow: hidden;
    font-family: "Source Sans 3", "Myriad Pro", sans-serif;
  }
  .roof-art { position: absolute; left: 0; top: 0; }
  .tagline {
    position: absolute; left: 22px; top: 20px;
    color: var(--paper); font-weight: 600; font-size: 21px; letter-spacing: 0.2px;
  }
  .contact { position: absolute; left: 357px; top: 20px; color: var(--teal); }
  .contact .phone { font-weight: 700; font-size: 44px; line-height: 1; letter-spacing: 0.5px; }
  .contact .website { font-weight: 600; font-size: 21px; line-height: 1.2; margin-top: 2px; letter-spacing: 0.2px; }
  .brand-name {
    position: absolute; right: 40px; top: 156px;
    display: flex; align-items: center; gap: 10px;
    color: var(--teal); font-size: 25px; font-weight: 400; letter-spacing: 0.3px;
  }
  .brand-name .mark { width: 14px; height: 14px; background: var(--teal); }
  .offer-list {
    position: absolute; right: 40px; top: 218px;
    list-style: none; text-align: right;
    font-family: "PT Sans Narrow", "Myriad Pro Condensed", sans-serif;
    color: var(--ink-grey); font-size: 32px; line-height: 44px;
  }
  .offer-list li { display: flex; align-items: center; justify-content: flex-end; gap: 12px; }
  .offer-list .bullet {
    width: 20px; height: 20px;
    display: grid; grid-template-columns: 1fr 1fr; gap: 2px;
  }
  .offer-list .bullet span { background: var(--teal); }
</style>
</head>
<body>
  <section class="bench-ad">
    <svg class="roof-art" width="720" height="334" viewBox="0 0 720 334">
      <defs>
        <linearGradient id="tealFade" x1="0" y1="0" x2="0" y2="1">
          <stop offset="0" stop-color="var(--teal-light)"/>
          <stop offset="1" stop-color="var(--teal-dark)"/>
        </linearGradient>
      </defs>
      <polygon class="corner-band" points="0,0 295,0 0,310" fill="url(#tealFade)"/>
      <g role="img" aria-label="Illustration of a house roof with chimney and windows">
        <polygon points="300,104 505,334 92,334" fill="url(#tealFade)"/>
      </g>
    </svg>

    <p class="tagline">WE MAKE IT SIMPLE</p>

    <div class="contact">
      <p class="phone">Cell (916) 482-3091</p>
      <p class="website">QUICKHOMEBUYERDESK.COM</p>
    </div>

    <p class="brand-name"><span class="mark"></span>QUICK HOME BUYER DESK</p>

    <ul class="offer-list">
      <li>Our company buys houses, any condition, any situation
        <span class="bullet"><span></span><span></span><span></span><span></span></span></li>
      <li>We buy houses for cash &amp; close quickly
        <span class="bullet"><span></span><span></span><span></span><span></span></span></li>
    </ul>
  </section>
</body>
</html>
```